Business Cards For A cell Phone Company
Linden Cellular
Business Cards For A cell Phone Company - Retailers
Creative Brief
Simple
Tobias Krell
Operations Manager
2864 Belmore Ave Cincinnati OH 45219
tobias.krell@lindencellular-mail.com
www.lindencellular-mail.com
Concepts
Business Cards/Letterhead/ Envelopes/Notepads/Tshirt/labels for quiet tin crate
Business cards and company letter head for Orchard Noodle Court

```html
<!DOCTYPE html>
<html lang="en">
<head>
<meta charset="utf-8">
<title>Linden Cellular – Business Card</title>
<link rel="stylesheet" href="https://fonts.googleapis.com/css2?family=Exo+2:wght@400;600;700&display=swap">
<style>
  :root {
    --bg: #e9e7e4;
    --card: #ffffff;
    --red: #d7141a;
    --red-dark: #a70d12;
    --grey: #9a9a9a;
    --grey-light: #d9d9d9;
    --ink: #4a4a4a;
    --white: #ffffff;
  }
  html, body {
    margin: 0; padding: 0;
    width: 1200px; height: 901px;
    overflow: hidden;
    background: var(--bg);
    font-family: "Exo 2", sans-serif;
  }
  .card {
    position: absolute;
    left: 100px; top: 165px;
    width: 1000px; height: 571px;
    border-radius: 40px;
    overflow: hidden;
    background: linear-gradient(180deg, #ffffff 0%, #f1f1f1 100%);
    box-shadow: 0 10px 30px rgba(0,0,0,.18);
  }
  .card__waves { position: absolute; inset: 0; }
  .brand {
    position: absolute; left: 80px; top: 90px;
    display: flex; align-items: center; gap: 16px;
  }
  .brand__dot {
    width: 46px; height: 46px; border-radius: 50%;
    background: var(--red);
  }
  .brand__name {
    font-weight: 700; font-size: 34px; letter-spacing: 2px;
    color: var(--red);
  }
  .person { position: absolute; left: 80px; top: 232px; }
  .person__name {
    font-weight: 600; font-size: 30px; letter-spacing: 1px;
    color: var(--ink); margin: 0;
  }
  .person__title {
    font-weight: 400; font-size: 20px; color: var(--red);
    margin: 4px 0 0;
  }
  .address {
    position: absolute; left: 80px; top: 440px;
    color: var(--white); font-size: 24px; line-height: 1.4;
    font-weight: 400; margin: 0;
  }
  .contacts {
    position: absolute; right: 50px; top: 175px;
    list-style: none; margin: 0; padding: 0;
    color: var(--white); font-size: 19px;
  }
  .contacts li {
    display: flex; justify-content: flex-end; align-items: center;
    gap: 12px; height: 34px;
  }
  .contacts svg { width: 20px; height: 20px; fill: var(--white); }
</style>
</head>
<body>
  <div class="card">
    <svg class="card__waves" viewBox="0 0 1000 571" width="1000" height="571" aria-hidden="true">
      <defs>
        <linearGradient id="redBand" x1="0" y1="0" x2="1" y2="1">
          <stop offset="0" stop-color="#e8232a"/>
          <stop offset="1" stop-color="#a70d12"/>
        </linearGradient>
        <linearGradient id="greyBand" x1="0" y1="0" x2="1" y2="0">
          <stop offset="0" stop-color="#cfcfcf"/>
          <stop offset=".5" stop-color="#8f8f8f"/>
          <stop offset="1" stop-color="#cfcfcf"/>
        </linearGradient>
      </defs>
      <path d="M0,345 C260,285 420,375 600,245 C720,160 850,75 1000,55 L1000,100 C850,120 720,210 600,300 C420,430 260,340 0,400 Z" fill="url(#greyBand)"/>
      <path d="M0,365 C260,305 420,395 600,265 C720,180 850,95 1000,75" fill="none" stroke="#ffffff" stroke-width="5"/>
      <path d="M0,400 C260,340 420,430 600,300 C720,210 850,120 1000,100 L1000,571 L0,571 Z" fill="url(#redBand)"/>
    </svg>

    <div class="brand">
      <span class="brand__dot"></span>
      <span class="brand__name">LINDEN CELLULAR</span>
    </div>

    <div class="person">
      <p class="person__name">TOBIAS KRELL</p>
      <p class="person__title">Managing Director</p>
    </div>

    <p class="address">2864 Belmore Ave<br>Cincinnati OH 45219</p>

    <ul class="contacts">
      <li>012 555 0147
        <svg viewBox="0 0 24 24"><path d="M6.6 10.8a15 15 0 0 0 6.6 6.6l2.2-2.2c.3-.3.7-.4 1-.2 1.1.4 2.3.6 3.6.6.6 0 1 .4 1 1V20c0 .6-.4 1-1 1A17 17 0 0 1 3 4c0-.6.4-1 1-1h3.5c.6 0 1 .4 1 1 0 1.3.2 2.5.6 3.6.1.3 0 .7-.2 1z"/></svg>
      </li>
      <li>012 555 0148
        <svg viewBox="0 0 24 24"><path d="M7 2h10a2 2 0 0 1 2 2v16a2 2 0 0 1-2 2H7a2 2 0 0 1-2-2V4a2 2 0 0 1 2-2zm0 3v13h10V5zm5 14.2a1 1 0 1 0 0 1.6 1 1 0 0 0 0-1.6z"/></svg>
      </li>
      <li>012 555 0149
        <svg viewBox="0 0 24 24"><path d="M4 3h16v12H8l-4 4z"/></svg>
      </li>
      <li>tobias.krell@lindencellular-mail.com
        <svg viewBox="0 0 24 24"><path d="M3 5h18v14H3zm2 2v.5l7 5 7-5V7zm0 3v7h14v-7l-7 5z"/></svg>
      </li>
      <li>www.lindencellular-mail.com
        <svg viewBox="0 0 24 24"><path d="M12 2a10 10 0 1 0 0 20 10 10 0 0 0 0-20zm6.9 9h-3a15 15 0 0 0-1.3-6 8 8 0 0 1 4.3 6zM12 4.1c.9 1.3 1.7 3.9 1.9 6.9h-3.8c.2-3 1-5.6 1.9-6.9zM9.4 5a15 15 0 0 0-1.3 6h-3a8 8 0 0 1 4.3-6zM5.1 13h3a15 15 0 0 0 1.3 6 8 8 0 0 1-4.3-6zm6.9 6.9c-.9-1.3-1.7-3.9-1.9-6.9h3.8c-.2 3-1 5.6-1.9 6.9zm2.6-.9a15 15 0 0 0 1.3-6h3a8 8 0 0 1-4.3 6z"/></svg>
      </li>
    </ul>
  </div>
</body>
</html>
```